Business card for event manager / organizer "velmora tandem"

Draft of a new valuable business card for my company.
Events, personnel service providers, festivals

```html
<!DOCTYPE html>
<html lang="en">
<head>
<meta charset="utf-8">
<title>velmora tandem – business card</title>
<link rel="stylesheet" href="https://fonts.googleapis.com/css2?family=Aldrich&display=swap">
<style>
  :root {
    --backdrop: #f2cdb6;
    --card-black: #1b1b1b;
    --hex-black: #141414;
    --accent: #e97c1c;
    --accent-deep: #d96e12;
    --muted: #8a8a8a;
    --light: #f4f4f4;
  }
  html, body {
    margin: 0;
    padding: 0;
    width: 1200px;
    height: 1200px;
    overflow: hidden;
    background: var(--backdrop);
  }
  .canvas {
    position: relative;
    width: 1200px;
    height: 1200px;
  }
  .card {
    position: absolute;
    left: 250px;
    width: 700px;
    height: 400px;
    display: block;
  }
  .card--front { top: 146px; }
  .card--back { top: 653px; }
  .card text {
    font-family: "Aldrich", sans-serif;
  }
  .fill-black { fill: var(--card-black); }
  .fill-hex { fill: var(--hex-black); }
  .fill-accent { fill: var(--accent); }
  .brand-name { fill: var(--light); font-size: 22px; }
  .brand-tagline { fill: var(--muted); font-size: 5.6px; }
  .holder-name { fill: var(--accent); font-size: 22px; }
  .holder-role { fill: var(--accent); font-size: 10.5px; letter-spacing: 1.6px; }
  .contact-text { fill: var(--accent); font-size: 14.5px; }
  .contact-text--small { font-size: 13.5px; }
  .icon { fill: none; stroke: var(--accent); stroke-width: 1.4; stroke-linecap: round; stroke-linejoin: round; }
  .icon-solid { fill: var(--accent); }
</style>
</head>
<body>
<main class="canvas">

  <!-- Front side -->
  <svg class="card card--front" viewBox="0 0 584 333" xmlns="http://www.w3.org/2000/svg" aria-label="Card front">
    <defs>
      <filter id="hex-lift" x="-20%" y="-20%" width="140%" height="140%">
        <feDropShadow dx="-6" dy="-4" stdDeviation="6" flood-color="#000" flood-opacity="0.55"/>
      </filter>
    </defs>
    <rect class="fill-black" width="584" height="333"/>
    <polygon class="fill-accent" points="342,0 584,0 584,333 342,333 400,167"/>
    <polygon class="fill-hex" filter="url(#hex-lift)" points="415,18 550,91 550,243 415,315 280,243 280,91"/>
    <g class="brand-lockup">
      <rect class="fill-accent" x="330" y="147" width="26" height="26"/>
      <text class="brand-name" x="362" y="169">velmora tandem</text>
      <text class="brand-tagline" x="498" y="183" text-anchor="end">…for every celebration worth sharing</text>
    </g>
  </svg>

  <!-- Back side -->
  <svg class="card card--back" viewBox="0 0 584 333" xmlns="http://www.w3.org/2000/svg" aria-label="Card back">
    <defs>
      <filter id="hex-lift-back" x="-20%" y="-20%" width="140%" height="140%">
        <feDropShadow dx="6" dy="-4" stdDeviation="6" flood-color="#000" flood-opacity="0.55"/>
      </filter>
    </defs>
    <rect class="fill-accent" width="584" height="333"/>
    <polygon class="fill-black" points="244,0 584,0 584,333 242,333 185,167"/>
    <polygon class="fill-hex" filter="url(#hex-lift-back)" points="140,36 258,104 258,232 140,299 20,232 20,104"/>

    <g class="holder">
      <text class="holder-name" x="140" y="175" text-anchor="middle">Jonas Berwald</text>
      <text class="holder-role" x="140" y="195" text-anchor="middle">Inhaber</text>
    </g>

    <g class="contacts">
      <!-- phone -->
      <path class="icon-solid" d="M279 89 l3 -1 2 4 -2 1.5 c1 2.5 3 4.5 5.5 5.5 l1.5 -2 4 2 -1 3 c-6 1 -14 -7 -13 -13z"/>
      <text class="contact-text" x="306" y="101">02104 557 21 38</text>

      <path class="icon-solid" d="M279 117 l3 -1 2 4 -2 1.5 c1 2.5 3 4.5 5.5 5.5 l1.5 -2 4 2 -1 3 c-6 1 -14 -7 -13 -13z"/>
      <text class="contact-text" x="306" y="129">0162 448 73 19</text>

      <!-- globe -->
      <g class="icon">
        <circle cx="286" cy="150" r="7"/>
        <ellipse cx="286" cy="150" rx="3" ry="7"/>
        <line x1="279" y1="150" x2="293" y2="150"/>
      </g>
      <text class="contact-text contact-text--small" x="306" y="155">www.velmora-tandem.de</text>

      <!-- envelope -->
      <g class="icon">
        <rect x="279" y="172" width="14" height="11" rx="1"/>
        <polyline points="279,173 286,179 293,173"/>
      </g>
      <text class="contact-text contact-text--small" x="306" y="183">info@velmora-tandem.de</text>

      <!-- pin -->
      <g class="icon">
        <path d="M286 218 c-4 -5 -7 -8 -7 -12 a7 7 0 0 1 14 0 c0 4 -3 7 -7 12z"/>
        <circle cx="286" cy="206" r="2.4"/>
      </g>
      <text class="contact-text contact-text--small" x="306" y="215">Lindenweg 12, 41199 Mönkhof</text>

      <!-- social -->
      <circle class="icon-solid" cx="286" cy="240" r="7"/>
      <text class="contact-text contact-text--small" x="306" y="245">social: /velmoratandem</text>
    </g>
  </svg>

</main>
</body>
</html>
```